Locksmith Services Tri Fold Flyer

We are a security company that provide all forms of security, we are looking to have tri fold flyers created for each service we offer starting with Locksmith Services, I am looking to work with someone who can design the layout and advise where the text would go where the pictures would go etc as well as tweaking our current logo, I am hoping to find someone that I can work with across all marketing materials for the business.

Our company is called Harborline Venture Collective , and the Locksmith side will be Harborline Locksmiths which is why the logo will need tweaking but with the text " Part of the Harborline Venture Collective "

Our Strap Line is " Protecting People, Property & Assets "

```html
<!DOCTYPE html>
<html lang="en">
<head>
<meta charset="utf-8">
<title>Harborline Locksmiths – Tri Fold Flyer</title>
<link href="https://fonts.googleapis.com/css2?family=Roboto+Slab:wght@400;700&family=Roboto:wght@400;700&display=swap" rel="stylesheet">
<style>
  :root{
    --page:#9a9a9a;
    --paper:#f7f7f7;
    --paper-mid:#efefef;
    --ink:#1c1c1c;
    --dark:#1f1f1f;
    --gold:#d4b36c;
    --gold-text:#c9a765;
    --gold-ring:#e4d5ae;
    --white:#ffffff;
  }
  *{box-sizing:border-box;margin:0;padding:0}
  html,body{width:762px;height:1200px;overflow:hidden}
  body{background:var(--page);font-family:"Roboto Slab",serif;color:var(--ink);position:relative}
  .flyer{position:absolute;left:31px;top:352px;width:700px;height:495px;overflow:hidden;box-shadow:0 6px 18px rgba(0,0,0,.35)}
  .flyer-art{position:absolute;inset:0}
  .t{position:absolute}
  .heading{font-weight:700;font-size:16px;line-height:22px}
  .body-copy{font-size:8.2px;line-height:11px}
  .body-copy.light{color:var(--white)}
  .center{text-align:center}
  .group-line{font-size:5px;color:var(--gold-text);letter-spacing:.1px;display:flex;align-items:center;justify-content:center;gap:5px}
  .group-line::before,.group-line::after{content:"";width:18px;height:.6px;background:var(--gold-text)}
  .strapline{color:var(--gold-text);font-weight:400;letter-spacing:.3px;line-height:1}
  .brand-name{font-weight:700;color:var(--gold-text);display:flex;align-items:center;justify-content:center;gap:6px}
  .brand-name .dot{border-radius:50%;background:var(--gold-text);display:inline-block}
  .contact-pill{background:var(--gold);border-radius:10px;font-family:"Roboto",sans-serif;font-weight:700;font-size:12px;line-height:19px;text-align:center;color:var(--ink)}
  .contact-line{font-size:7.6px;line-height:10px;display:flex;align-items:center;justify-content:center;gap:3px}
  .contact-line svg{flex:none}
  .promise{color:var(--gold-text);font-weight:700;font-size:13.5px;line-height:19px}
  .emergency-title{font-family:"Roboto",sans-serif;font-weight:700;color:var(--white);font-size:13px;line-height:16px;background:var(--dark);padding:0 3px}
  .emergency-number{background:var(--gold);font-family:"Roboto",sans-serif;font-weight:700;font-size:15px;line-height:20px;color:var(--ink);display:flex;align-items:center;justify-content:center;gap:6px}
</style>
</head>
<body>
<div class="flyer">
  <svg class="flyer-art" width="700" height="495" viewBox="0 0 700 495">
    <!-- panels -->
    <rect x="0" y="0" width="233" height="495" fill="var(--paper)"/>
    <rect x="233" y="0" width="233" height="495" fill="var(--paper-mid)"/>
    <rect x="466" y="0" width="234" height="495" fill="var(--paper)"/>
    <rect x="0" y="265" width="233" height="230" fill="var(--dark)"/>
    <rect x="466" y="265" width="234" height="230" fill="var(--dark)"/>
    <rect x="0" y="491" width="700" height="4" fill="var(--gold)"/>

    <!-- section rules -->
    <rect x="31" y="57" width="172" height="1.2" fill="var(--gold)"/>
    <rect x="264" y="79" width="172" height="1.2" fill="var(--gold)"/>

    <!-- left panel photo circles -->
    <circle cx="193" cy="267" r="89" fill="#5a5048" stroke="var(--gold-ring)" stroke-width="4" role="img" aria-label="Photo: key cutting machine close-up"/>
    <circle cx="73" cy="268" r="72" fill="#8a7464" stroke="var(--gold-ring)" stroke-width="4" role="img" aria-label="Photo: locksmith fitting a mortice lock into a door"/>

    <!-- right panel photo circles -->
    <circle cx="514" cy="267" r="49" fill="#6b5a4c" stroke="var(--gold-ring)" stroke-width="4" role="img" aria-label="Photo: hand turning a door handle"/>
    <circle cx="623" cy="267" r="80" fill="#8c6f4a" stroke="var(--gold-ring)" stroke-width="4" role="img" aria-label="Photo: locksmith drilling a door lock with a cordless drill"/>

    <!-- partner badges -->
    <rect x="297" y="188" width="22" height="22" fill="#f2d21b" stroke="#8aa02a" stroke-width="1"/>
    <circle cx="333" cy="199" r="11" fill="#f5cf0a"/>
    <rect x="346" y="188" width="26" height="17" fill="#d8262c"/>
    <rect x="380" y="190" width="33" height="13" rx="2" fill="#1e2f86"/>

    <!-- contact ornaments -->
    <line x1="290" y1="397" x2="319" y2="397" stroke="var(--gold)" stroke-width=".8"/>
    <line x1="381" y1="397" x2="410" y2="397" stroke="var(--gold)" stroke-width=".8"/>
    <g fill="none" stroke="var(--gold)" stroke-width="1">
      <path d="M350 401c-3-4-4-6-4-8a4 4 0 0 1 8 0c0 2-1 4-4 8z"/>
      <circle cx="350" cy="393" r="1.3"/>
    </g>

    <!-- emergency frame -->
    <path d="M489 446 V479 H677 V446" fill="none" stroke="#bcbcbc" stroke-width="1"/>
    <line x1="489" y1="446" x2="496" y2="446" stroke="#bcbcbc" stroke-width="1"/>
    <line x1="670" y1="446" x2="677" y2="446" stroke="#bcbcbc" stroke-width="1"/>
    <rect x="572" y="423" width="36" height="1.2" fill="var(--white)"/>
  </svg>

  <!-- panel 1: about -->
  <h2 class="t heading" style="left:31px;top:27px">About Us</h2>
  <p class="t body-copy" style="left:31px;top:67px;width:176px">Lorem ipsum dolor sit amet, consectetur adipiscing elit, sed do eiusmod tempor incididunt ut labore et dolore magna aliqua. Ut enim ad minim veniam, quis nostrud exercitation ullamco laboris nisi ut aliquip ex ea commodo consequat.<br>Duis aute irure dolor in reprehenderit in voluptate velit esse cillum dolore eu fugiat nulla pariatur.</p>
  <p class="t body-copy light" style="left:31px;top:374px;width:176px">Sed ut perspiciatis unde omnis iste natus error sit voluptatem accusantium doloremque laudantium, totam rem aperiam, eaque ipsa quae ab illo inventore veritatis et quasi architecto beatae vitae dicta sunt explicabo. Nemo enim ipsam voluptatem quia voluptas sit aspernatur aut odit aut fugit,</p>

  <!-- panel 2: welcome & contact -->
  <h1 class="t heading center" style="left:233px;top:27px;width:233px">Welcome to Harborline<br>Locksmiths</h1>
  <p class="t body-copy center" style="left:250px;top:94px;width:200px">Here at Harborline Locksmiths, we provide our customers with friendly, professional locksmith services throughout Marrowfield and the surrounding areas. From emergency entry to key cutting, safes and locks, we are experts when it comes to physical security.</p>
  <div class="t brand-name" style="left:233px;top:262px;width:233px;font-size:11px"><span class="dot" style="width:9px;height:9px"></span>Harborline Locksmiths</div>
  <div class="t group-line" style="left:233px;top:306px;width:233px">Part of the Harborline Venture Collective</div>
  <div class="t strapline center" style="left:233px;top:316px;width:233px;font-size:9px;line-height:9.5px">PROTECTING PEOPLE,<br>PROPERTY &amp; ASSETS</div>
  <div class="t contact-pill" style="left:296px;top:358px;width:109px">Contact Us</div>
  <div class="t body-copy center" style="left:233px;top:405px;width:233px;font-size:7.6px;line-height:10.5px">Address Line 1, Address Line 1<br>Address Line 2</div>
  <div class="t contact-line" style="left:233px;top:432px;width:233px">
    <svg width="8" height="6" viewBox="0 0 8 6"><rect x=".4" y=".4" width="7.2" height="5.2" fill="none" stroke="var(--gold)" stroke-width=".7"/><path d="M.4 .4 4 3.4 7.6 .4" fill="none" stroke="var(--gold)" stroke-width=".7"/></svg>info@harborlineventure.com</div>
  <div class="t contact-line" style="left:233px;top:448px;width:233px">
    <svg width="7" height="7" viewBox="0 0 7 7"><circle cx="3.5" cy="3.5" r="3.1" fill="none" stroke="var(--gold)" stroke-width=".7"/><path d="M2.3 2c.3 1.3 1.3 2.4 2.6 2.8" fill="none" stroke="var(--gold)" stroke-width=".7"/></svg>0123 555 019</div>
  <div class="t contact-line" style="left:233px;top:462px;width:233px">
    <svg width="7" height="7" viewBox="0 0 7 7"><circle cx="3.5" cy="3.5" r="3.1" fill="none" stroke="var(--gold)" stroke-width=".7"/><ellipse cx="3.5" cy="3.5" rx="1.3" ry="3.1" fill="none" stroke="var(--gold)" stroke-width=".6"/><line x1=".4" y1="3.5" x2="6.6" y2="3.5" stroke="var(--gold)" stroke-width=".6"/></svg>harborlinelocksmiths.co.uk</div>

  <!-- panel 3: cover -->
  <div class="t brand-name" style="left:466px;top:64px;width:234px;font-size:14px"><span class="dot" style="width:12px;height:12px"></span>Harborline Locksmiths</div>
  <div class="t group-line" style="left:466px;top:136px;width:234px">Part of the Harborline Venture Collective</div>
  <div class="t strapline center" style="left:466px;top:148px;width:234px;font-size:13px;line-height:14px">PROTECTING PEOPLE,<br>PROPERTY &amp; ASSETS</div>
  <p class="t promise center" style="left:466px;top:361px;width:234px">We are trustworthy,<br>reliable &amp; an experienced<br>team of locksmiths</p>
  <div class="t" style="left:466px;top:438px;width:234px;display:flex;justify-content:center"><span class="emergency-title">FOR EMERGENCY CALL</span></div>
  <div class="t emergency-number" style="left:515px;top:456px;width:135px">
    <svg width="13" height="13" viewBox="0 0 13 13"><rect x=".7" y=".7" width="11.6" height="11.6" fill="none" stroke="var(--ink)" stroke-width="1.2"/><circle cx="6.5" cy="6.5" r="3.8" fill="none" stroke="var(--ink)" stroke-width="1"/><path d="M5 5c.3 1.4 1.3 2.6 2.8 3" fill="none" stroke="var(--ink)" stroke-width="1"/></svg>0800 555 0192</div>
</div>
</body>
</html>
```